drafting business needs a 2 sided rack card design. Size specificaton

Document Trim Size:
Full Bleed Size (starting document size)
3.86" x 8.39"
When trimmed the Rack cards are 3.74" x 8.27".
300 DPI

I need my logo, product info, and 2 pictures included

This is product information that i need:

- Floor Plans measured to QERT & PLUX standards
- Stunning HD Photography
- Vexolith - your space delivered in perfect 3D
- E &O insured
- Our products delivered next by before 10:00 AM

It also has to my my special offer: Save 50% off Vexolith, Floor Plans, and Photography

My contact info is
www.quillfenstudio.com
dorian@quillfenstudio.com
778-514-0962
Updates

Hey designers, the common element I see in most of the designs that I actually don't like is the use of orange and blue. I think there was some miscommunication. Please Don't use these colors. It really makes the designs Look cheap. I want a clean, high end look.

Target Market(s)

realtors

Industry/Entity Type

Real Estate

Font styles to use
Serif

Colors

Designer to choose colors to be used in the design.

Requirements
Must have
• At least 2 photos and my logo included. it must include all my wording with discount in bold, but classy.
Nice to have
• I want clean classy design. My logo is and 2 photos should be in design. I design should match my logo colors, I think. I have tons of other photos if you think these arent very useful
• Also I have attached a logo from vexolith. Please include this, but smaller than the Quillfen Studio. The Vexolith is just equiptment that I use
Should not have
• This is a discount promotion, but I dont want it to look cheap whatsoever

```html
<!DOCTYPE html>
<html lang="en">
<head>
<meta charset="utf-8">
<title>Quillfen Studio Rack Card</title>
<link href="https://fonts.googleapis.com/css2?family=Noto+Serif:wght@400;700&display=swap" rel="stylesheet">
<style>
  :root {
    --charcoal: #2c2c2e;
    --gold: #a8885a;
    --gold-light: #cbb48c;
    --ink: #2b2b2b;
    --rule: #b5aa98;
    --paper: #ffffff;
    --backdrop: #b4b5b9;
    --badge: #f1eee8;
  }
  * { margin: 0; padding: 0; box-sizing: border-box; }
  html, body { width: 1200px; height: 1134px; overflow: hidden; }
  body {
    background: var(--backdrop);
    font-family: "Noto Serif", Georgia, serif;
    color: var(--ink);
    position: relative;
  }
  .side-label {
    position: absolute; top: 118px;
    font-size: 19px; font-weight: 700; color: #4a4a4a; letter-spacing: .5px;
  }
  .card {
    position: absolute; top: 158px; width: 376px; height: 828px;
    background: var(--paper); overflow: hidden;
  }
  .card--front { left: 154px; }
  .card--back { left: 644px; }
  .accents { position: absolute; inset: 0; width: 376px; height: 828px; pointer-events: none; }
  .photo { position: absolute; }
  .photo--living { left: 0; top: 146px; width: 376px; height: 340px;
    background: linear-gradient(160deg, #dfe2e4 0%, #c9c4bb 45%, #8a6c52 75%, #4a3a2e 100%); }
  .photo--hall { left: 0; top: 0; width: 376px; height: 334px;
    background: linear-gradient(135deg, #e9e3d8 0%, #d6cbb8 40%, #9b5a2c 75%, #5a3318 100%); }
  .brand { position: absolute; text-align: center; }
  .brand__mark { display: block; margin: 0 auto; border-radius: 50%; background: var(--charcoal); }
  .brand__name { color: var(--charcoal); font-weight: 400; white-space: nowrap; }
  .brand--front { left: 0; width: 376px; top: 22px; }
  .brand--front .brand__mark { width: 72px; height: 72px; }
  .brand--front .brand__name { font-size: 29px; margin-top: 2px; }
  .logo-tab { position: absolute; left: 178px; top: 282px; width: 190px; height: 90px;
    background: var(--paper); border-top-left-radius: 12px; border-top-right-radius: 12px; }
  .brand--back { left: 178px; width: 190px; top: 290px; }
  .brand--back .brand__mark { width: 58px; height: 58px; }
  .brand--back .brand__name { font-size: 22px; margin-top: 1px; }
  .offer { position: absolute; left: 44px; top: 514px; width: 300px; height: 110px; }
  .offer__figure { position: absolute; left: 0; top: -16px; font-size: 132px; font-weight: 700; color: var(--gold); line-height: 1; letter-spacing: -2px; }
  .offer__percent { position: absolute; left: 154px; top: 4px; font-size: 38px; color: var(--gold); line-height: 1; }
  .offer__save { position: absolute; left: 198px; top: 24px; font-size: 33px; font-weight: 700; color: var(--charcoal); line-height: 1; }
  .offer__off { position: absolute; left: 165px; top: 50px; font-size: 58px; font-weight: 700; color: var(--gold); line-height: 1; }
  .offer-items { position: absolute; left: 44px; top: 624px; width: 300px; font-weight: 700; line-height: 1.1; color: var(--charcoal); }
  .offer-items__line1 { font-size: 18px; }
  .offer-items__line2 { font-size: 25px; }
  .contact { position: absolute; left: 38px; top: 740px; color: #fff; font-size: 17px; line-height: 22px; }
  .features { position: absolute; left: 36px; top: 392px; width: 304px; }
  .feature { border-bottom: 1.5px solid var(--rule); }
  .feature__heading { font-size: 20px; font-weight: 700; line-height: 27px; padding-bottom: 12px; }
  .feature--3d { display: flex; align-items: center; justify-content: space-between; padding: 10px 0 14px; }
  .feature__text { font-size: 16px; line-height: 22px; }
  .badge { width: 108px; height: 33px; border-radius: 6px; background: var(--badge); }
  .feature__caps { font-size: 19px; font-weight: 700; padding: 10px 0 9px; }
  .feature__caps .accent { color: var(--gold); }
  .feature__plain { font-size: 16px; padding: 10px 0 9px; }
  .promise { font-size: 22px; font-weight: 700; color: var(--gold); line-height: 29px; padding-top: 12px; }
</style>
</head>
<body>
  <div class="side-label" style="left:155px">FRONT</div>
  <div class="side-label" style="left:645px">BACK</div>

  <section class="card card--front">
    <div class="photo photo--living" role="img" aria-label="Bright living room with sofa, rug, fireplace and tall windows"></div>
    <svg class="accents" viewBox="0 0 376 828" aria-hidden="true">
      <polygon points="0,0 16,0 0,70" fill="var(--gold)"/>
      <polygon points="24,0 58,0 0,244 0,100" fill="var(--charcoal)"/>
      <polygon points="58,42 68,42 16,212 8,212" fill="var(--gold)"/>
      <polygon points="0,724 316,724 292,828 0,828" fill="var(--charcoal)"/>
      <polygon points="334,670 348,670 312,828 298,828" fill="var(--gold)"/>
      <polygon points="358,670 376,670 376,828 326,828" fill="var(--charcoal)"/>
      <polygon points="376,738 376,760 360,828 352,828" fill="var(--gold)"/>
    </svg>
    <div class="brand brand--front">
      <span class="brand__mark"></span>
      <div class="brand__name">Quillfen Studio</div>
    </div>
    <div class="offer">
      <span class="offer__figure">50</span>
      <span class="offer__percent">%</span>
      <span class="offer__save">SAVE</span>
      <span class="offer__off">OFF</span>
    </div>
    <div class="offer-items">
      <div class="offer-items__line1">VEXOLITH, FLOOR PLANS,</div>
      <div class="offer-items__line2">AND PHOTOGRAPHY</div>
    </div>
    <div class="contact">
      www.quillfenstudio.com<br>dorian@quillfenstudio.com<br>778-514-0962
    </div>
  </section>

  <section class="card card--back">
    <div class="photo photo--hall" role="img" aria-label="Entry hall seen from above with staircase, bench, tile floor and painting"></div>
    <svg class="accents" viewBox="0 0 376 828" aria-hidden="true">
      <polygon points="0,0 30,0 0,130" fill="var(--paper)"/>
      <polygon points="0,0 16,0 0,70" fill="var(--gold)"/>
      <polygon points="30,0 58,0 0,244 0,126" fill="var(--charcoal)"/>
      <polygon points="58,0 82,0 0,334 0,240" fill="var(--paper)"/>
      <polygon points="60,42 70,42 18,212 10,212" fill="var(--gold)"/>
      <polygon points="0,724 316,724 292,828 0,828" fill="var(--charcoal)"/>
      <polygon points="334,670 348,670 312,828 298,828" fill="var(--gold)"/>
      <polygon points="358,670 376,670 376,828 326,828" fill="var(--charcoal)"/>
      <polygon points="376,738 376,760 360,828 352,828" fill="var(--gold)"/>
    </svg>
    <div class="logo-tab"></div>
    <div class="brand brand--back">
      <span class="brand__mark"></span>
      <div class="brand__name">Quillfen Studio</div>
    </div>
    <div class="features">
      <div class="feature"><div class="feature__heading">Floor Plans measured to<br>QERT; PLUX standards</div></div>
      <div class="feature feature--3d">
        <div class="feature__text">Vexolith - your space<br>delivered in perfect 3D</div>
        <div class="badge" role="img" aria-label="Equipment partner badge"></div>
      </div>
      <div class="feature"><div class="feature__caps">STUNNING <span class="accent">HD</span> PHOTOGRAPHY</div></div>
      <div class="feature"><div class="feature__plain">E&amp;O insured</div></div>
      <div class="promise">Our products delivered<br>next by before 10:00 AM</div>
    </div>
    <div class="contact">
      www.quillfenstudio.com<br>dorian@quillfenstudio.com<br>778-514-0962
    </div>
  </section>
</body>
</html>
```